Wordpress E-Commerce Site for Flower Company

CREATIVE BRIEF FOR 762PETALS
- UPDATED 9.22.14 -
We need a wordpress ecommerce website and logo for our flower company. The name of our company is 762petals.com.ph, and we take orders from the around the world, and ship flowers to loved ones specifically in the Philippines. Our final dot come will be www.762petals.com.ph.

We want our site to follow the themes and look of these pages:
https://www.thevarnel.com/en/
http://www.ourbloomshed.com/

Our color theme is light purple and pastel pink.
We would like our website to have these social media connections: facebook, twitter, and instagram.

E-COMMERCE NEEDS:
We want our customers to be able to login, and have a separate "Account Page" where they can look at their previous orders, store payment information so that they don't have to re-input their payment information again, and also be able to login and give product reviews on our products.

We want two separate order pages where our customers can place "recurring orders" In other words, a customer can use a calendar or form and input the dates he would like to re-order a product. He would be charged ahead of time, and can order a product up to a year in advance. He can set it up so that he pays ahead of time for a flower to arrive once a month, a week, or daily for the next six months. After he customizes his timely order, he will then be taken to a check out page where he will be charged for all of the orders at once i.e. if he places an order for a flower arrangement to arrive once a month for 12 months, he will be charge for the product 12 times.

We want our shopping cart and website to be secure.

We would also like a pop up to appear after browsing the website for 30 seconds. The pop up will offer them a 10% discount on their first order if they give us their email. We want to be able to collect emails and add them to an email list.

Main Slider has 3-4 SLIDES Example: Deal of the Week!, Sign Up and get 10% off your first order.

If you use pictures of people in the banners or in other sections of the site, please keep them of Filipino or Pacific Island ethnicity as our target audience is Filipinos. Japanese, Indian, Chinese, Caucasian, Hispanic, or African American are not recommended. For a general look of the filipino ethnicity look we are talking about visit this website: http://qxn.tv/

The Main Page Links of the site should be...
Main Menu: Home | Shop Flowers | Keep Me Near | Recent News
Separate Links above Menu: Sign In | Cart | Help

Our Help page should include a FAQ section that allows us to add Questions and Answers in a Toggle/Accordian/Tabbed view so that the Question hides the Answer, but when you click on the Question is clicked the Answer is revealed. The FAQ should be divided into sections, "General Questions" "Billing" "Shipping"

On the same Help page should be a contact us form with further questions or concerns. This form will allow our customers to contact us via email with any questions or concerns.

Make sure we have a page dedicated to our blog posts, as we do want to post updates, special deals, and blog articles as time passes on.
Please use filler images for the product pictures and banners.

The logo for our company should have a ROSE. A beautiful vector rose, designed in a modern way.

As for the logo, we would like something simple, modern, and have it retain the words 762petals... kind of like the logo on http://ww30.5206stems.com/. Incorporate our new colors into the logo. Simple, modern, and welcoming.

Also, incorporate the flag of the Philippines in some of the graphics. Have one of the banners show the Philippines on a map and place the words, "We ship exclusively to the Philippines." Emphasize that this service offers customers from around the world to buy flowers that will be delivered specifically to loved ones in the Philippines. We work with flower growers in the Philippines so next day delivery is possible.

762Petals Site Map

HOME PAGE

Main Links - These Links are located at the top of the page... the Header

Home
Button Function: Home Page Link

Shop Flowers
Button Function: Leads to a page revealing our categories - Birthday, Anniversary, Congratulations, Graduation, Baby Shower, Get Well Soon, Thank You, Thinking of You - which leads to that individual category page with SIX Flower Arrangements on each page.

Keep Me Near
Button Function: Leads to our concierge service page - There must be a brief explanation on how this service works. Customer must choose 3 or more important dates. There will be drop down suggestions, and then a space to select the date from a calendar. Suggestions like wedding anniversary date; 1st child born; Valentine’s Day; Mother’s day; her/his birthday, etc. Also, must be stated that if you send six future deliveries, you get the seventh flower arrangement FREE.

Recent Updates
Button Function: Takes you to our Blog Page where updates and articles are posted

FOUR Center Banners - These Four Banners/Buttons/Pictures are at the center of the Front Page. They lead to the main sections of our site.

1. Title: “For Married Couples”
Subtitle Description: Have your romance on automatic
Button Function: Leads to our concierge service page (same as Keep Me Near) - offers occasions to send flowers automatically.

2. Title: "Special Occasions"
Subtitle Description: Still has to be written
Button Function: Link is same as "Shop Flowers"

3.Title: "Courting Him/Her"
Subtitle Description: Subscription Flower Delivery Service
Button Function: Takes them to the Courting Him/Her page where it is just like the "For Married Couples" subscription delivery page, except instead of specific dates, it expects a minimum of six deliveries of flowers based on a consistent day.

The form will ask them to choose a flower, then set that flower arrangement to be delivered every BLANK (day) for BLANK (weeks).... so every Tuesday for six weeks, or every day of the week for one week, or every Tuesday and Thursday for 3 weeks. They can also have the same flower arrangement be delivered, or a different flower arrangement delivered every time.

Explanation of Service: every week or month, we will send your significant other a subscription flower delivery. Every six orders, the seventh is free.

4. Title: “Just Because"
Subtitle: Flowers Arrangement for Any Reason
Button Function: This will go to a page showing 6 random flower arrangements.
Put them left to right in this order.
Footer Links - These links are located in a separate section at the bottom of the page... the Footer.

The content for the footer links are very similar to the content in the footer of www.thevarnel.com. Here is a breakdown of the links on the bottom and what we want the content to be for those pages:

ABOUT
About 762petals - https://www.thevarnel.com/en/content/4-about-us

Privacy & Legal Stuff - https://www.thevarnel.com/en/content/2-privacy-legal-stuff

ORDERING
Bulk Orders/Events - This page will have a small paragraph detailing the steps needed to order in bulk. At the bottom of this paragraph will be an email contact form. You can start with..."Need to order a large amount of flowers for your special event? We can help! Blah blah blah blah." In the end you have the customer fill out the email form, and we will get back to them with a custom quote.

For Businesses - https://www.thevarnel.com/en/business

CUSTOMER CARE
Testimonials - https://www.thevarnel.com/en/content/18-testimonials

FAQ's - https://www.thevarnel.com/en/content/11-faq

Customer Service - https://www.thevarnel.com/en/contact-us

Customer Service is basically an email contact page. Have the customer contact us with any questions or concerns via email. No phone number.

Replacement & Refund Policy - https://www.thevarnel.com/en/content/1-replacement-refund-policy

Flower Care - Paraphrase this link in your own words. It's basically the best way to care for flowers.
http://thequietlomarealm.craftrovex.com/how-to/tips-for-keeping-your-flowers-fresh-and-long-lasting-0131219/

Referral Program - https://www.thevarnel.com/en/getfreevarn

Contact Us - Simple Contact Us Page - https://www.thevarnel.com/en/contact-us

SEPARATE PAGES

Occasion Page - Each Occasion page represents a different category of flowers. Currently, we have EIGHT OCCASIONS we want to sell flowers for: Birthday, Anniversary, Congratulations, Graduation, Baby Shower, Get Well Soon, Thank You, and Thinking of You.

We want our Occasion Pages to each have a Banner on top that is around 200 pixels high by page width or (1100px) that summarizes the occasion. If it's the birthday category, then a picture of birthday flower arrangement, some balloons, and a cake. If it's the romantic occasion then a banner representing that occasion.

After that, reveal the 6 arrangements of flowers underneath.

Single Flower Arrangement Flower Page - Must show three different views of the flower arrangement. Each view representing a dozen, two dozen, or three dozen arrangement.

There should be an area for product description. http://www.ourbloomshed.com/ultimate-bouquet/

Also, as they choose that product, they can add a Greeting Card for Free to their order.

The options that follow this Greeting Card are the following:
"Do you want your Greeting Card to be...?"
() scented or () unscented
"Type of Occasion?" - A dropdown menu of all the occasions - Birthday, Anniversary, Congratulations, Graduation, Baby Shower, Get Well Soon, Thank You, Thinking of You
Once the occasion is selected. A second drop down menu appears with CUSTOM GREETINGS.
For example, if they choose "Thank You" from the previous menu, THREE PREMADE GREETINGS will appear...
"Choose from these Pre-Made Greetings."
() "I appreciate all that you've done for me during these troubling times."
() "I thank you from the bottom of my heart, and wish you well."
() "From my heart to yours... thank you."
() FOURTH OPTION says..."Or say it in your own words!"
And there is a space for their own message.
Then a space for "To:" and "From:"
Then the delivery date calendar.

Attached are pictures of what we want our front page to look like, as well as some pics to help with the design.
Updates

A mock up picture has been uploaded showing the structure we want for our front page. Thank you.

Update! We uploaded a photoshop file of our logo. We would like the same font used... heartland, and the same colors. All we are missing in the logo is the "Sambaguita" flower. We placed an example of one in the photoshop file. If you can draw your own in the logo, that would be great.

Our 4 Banner Links in the Center have these titles and subtitles.... SPECIAL OCCASION (Mahalagang Okasyon) Flower Picture: Bouqet of Assorted Flowers "MARRIED" - Romance on Automatic (Mag Asawa) How it Works Flower Picture: Red Roses, up close "COURTING" - Him/Her (Nan Liligaw) How it Works Flower Picture: Yellow Flower Arrangement JUST BECAUSE (Dahil Lang) Flower Picture: Random Color Arrangement, Up close PLACE THEM IN THAT ORDER, FROM LEFT TO RIGHT

Target Market(s)

Filipino or Individuals who live in the USA that want to purchase flowers for their loved ones abroad in the Phillipines

Industry/Entity Type

Business

Font styles to use
Sans Serif

Colors
ffffff
e567a6
f59195

Requirements
Must have
• Any persons that are placed in pictures on website must look like they are Filipinos. As a reference you may look at the Filipinos on http://qxn.tv/

Customers MUST have the ability to login into their Account on our website. Their account reveals their past purchase orders, their reviews of our products, and billing information. They can also personalize their recurring orders when they login so that it remembers them.

Subscription service must also be available. When they order flowers for future dates they must have a page to go to where they can select calendar dates for future flower deliveries.

There must also be a separate "Custom Arrangement" page that allows the customer to order a custom flower arrangement. They will be able to choose from 6 types of flowers: (Carnations, Daisies, Lilies, Orchids, Roses, Tulips), 6 different types of colors (blue, red, white, purple, orange, yellow), and the amount of each flower based on how big their arrangement is... one dozen, two dozen, etc. (ie for a two dozen order... 6 Red Roses, 9 White Daises, 3 Purple Orchids, 3 White Lilies)

When you click on a product picture it should take you to a separate page dedicated to the product. It should look like this: https://www.thevarnel.com/en/tundra-collection/165-maple-drift.html
Nice to have
• We are selling our flower packages starting at $19.99 for a dozen flowers. $29.99 for two dozen. After that they pick the type of flower or arrangement. Those are our two basic packages. Leave room for add ons like teddy bear, chocolates, balloons.

Good example for categories and such: http://www.quillpostmanila.net/
Should not have
• Too many categories and buttons. Very simple and intuitive. Hence why we chose wordpress for the ecommerce site. We want a 12 year old to be able to order flowers.

```html
<!DOCTYPE html>
<html lang="en">
<head>
<meta charset="utf-8">
<title>762petals – Flowers to the Philippines</title>
<link rel="stylesheet" href="https://fonts.googleapis.com/css2?family=Open+Sans:wght@400;600;700&family=Libre+Baskerville&display=swap">
<style>
  :root{
    --white:#ffffff;
    --pink:#f28a95;
    --rose:#e567a6;
    --pink-soft:#fbd9de;
    --ink:#333333;
    --muted:#8a8a8a;
    --line:#dddddd;
    --panel:#f6f6f6;
    --dark-bar:#3b3b3b;
    --footer:#ececec;
  }
  *{box-sizing:border-box;margin:0;padding:0}
  html,body{width:719px;height:1200px;overflow:hidden;background:var(--white);
    font-family:"Open Sans",Arial,sans-serif;color:var(--ink)}
  .page{position:relative;width:719px;height:1200px}
  .abs{position:absolute}

  /* header */
  .brand{left:30px;top:14px;display:flex;align-items:center;gap:6px}
  .brand-dot{width:14px;height:14px;border-radius:50%;background:var(--rose)}
  .brand-name{font-size:17px;font-weight:700;color:var(--rose);letter-spacing:.2px}
  .util-links{right:30px;top:12px;font-size:7px;color:var(--muted)}
  .util-links span{margin-left:4px}
  .main-nav{right:30px;top:44px;display:flex;font-size:7.5px;color:var(--ink)}
  .main-nav a{padding:6px 12px;color:inherit;text-decoration:none}
  .main-nav a.active{background:var(--panel);border:1px solid var(--line)}

  /* hero */
  .hero{left:28px;top:80px;width:662px;height:232px;overflow:hidden;
    background:linear-gradient(100deg,#e9e9e9 0%,#f4f4f4 35%,#e6e6e3 55%,#b8c48a 66%,#c81f2b 76%,#e23a3a 86%,#f3f0ef 100%)}
  .hero-copy{position:absolute;left:28px;top:58px}
  .hero-title{font-family:"Libre Baskerville",Georgia,serif;font-size:21px;line-height:27px;color:#2c2c2c}
  .btn{display:inline-block;background:var(--pink);color:var(--white);font-weight:600;text-align:center}
  .hero-btn{margin-top:16px;font-size:8px;padding:9px 20px;letter-spacing:.3px}

  /* info boxes */
  .info{top:324px;width:214px;height:146px;border:1px solid var(--line);background:var(--white)}
  .info h3{font-size:9px;font-weight:600;color:#555;padding:6px 8px;border-bottom:1px solid var(--line)}
  .news-item{display:flex;gap:5px;padding:6px 8px 0}
  .news-date{width:22px;height:26px;background:var(--pink);color:var(--white);font-size:5.5px;text-align:center;line-height:9px;padding-top:3px;font-weight:700}
  .news-date b{display:block;font-size:9px}
  .news-thumb{width:26px;height:26px;background:linear-gradient(#c9a48b,#8a6a58)}
  .news-text{font-size:5.5px;line-height:8px;color:var(--muted);width:120px}
  .news-text strong{color:var(--pink);font-weight:600;display:block}
  .quote{padding:8px;font-size:6px;line-height:9px;color:var(--muted)}
  .quote-foot{display:flex;justify-content:space-between;align-items:center;padding:0 8px}
  .avatar{width:20px;height:20px;border-radius:50%;background:linear-gradient(#d8b39a,#9e7866)}
  .arrows{display:flex;gap:3px}
  .arrows span{width:8px;height:8px;border-radius:50%;background:#bbb}
  .email-input{margin:6px 8px;height:16px;border:1px solid var(--line);font-size:6px;color:#aaa;padding:4px 5px}
  .subscribe{margin-left:8px;font-size:7px;padding:5px 14px}

  /* sidebar */
  .sidebar{left:28px;top:480px;width:100px}
  .side-head{background:var(--pink);color:var(--white);font-size:7px;font-weight:600;padding:4px 6px;margin-top:6px}
  .side-sub{background:var(--panel);font-size:6px;color:#666;padding:3px 6px;border-bottom:1px solid var(--line)}
  .side-list{list-style:none;font-size:6px;color:#555;border:1px solid var(--line);border-top:0}
  .side-list li{display:flex;align-items:center;gap:4px;padding:3px 6px;border-top:1px solid #eee}
  .side-list li i{width:5px;height:5px;border:1px solid #aaa;display:inline-block}
  .swatches{display:flex;flex-wrap:wrap;gap:3px;padding:5px 6px;border:1px solid var(--line);border-top:0}
  .swatches span{width:12px;height:9px}
  .price-row{font-size:6px;color:#555;padding:5px 6px;border:1px solid var(--line);border-top:0}
  .price-row .bar{height:3px;background:var(--pink-soft);margin-top:4px;position:relative}
  .price-row .bar::after{content:"";position:absolute;left:20%;right:30%;top:0;bottom:0;background:var(--pink)}
  .offer{margin-top:8px;border:1px solid var(--line);padding:5px;text-align:center}
  .offer-title{font-size:6.5px;font-weight:700;color:var(--pink);line-height:8px}
  .offer-img{height:86px;margin-top:4px;background:radial-gradient(circle at 50% 40%,#f6c64a,#e87b59 45%,#7fae5b 80%,#c9a06a)}

  /* products */
  .products{left:140px;top:480px;width:550px}
  .products-bar{background:var(--dark-bar);color:var(--white);font-size:8px;font-weight:700;padding:6px 10px;letter-spacing:.3px}
  .grid{display:grid;grid-template-columns:repeat(3,1fr);row-gap:22px;padding-top:18px}
  .card{text-align:center}
  .card-img{width:100px;height:88px;margin:0 auto}
  .sun{background:radial-gradient(circle at 50% 45%,#f7c425,#e8911c 40%,#5c7d33 75%,#fff 76%)}
  .roses{background:radial-gradient(circle at 50% 45%,#d3202e,#a9141f 55%,#4f7a3a 72%,#fff 74%)}
  .card-title{font-size:6px;font-weight:700;color:var(--pink);margin-top:8px;letter-spacing:.2px}
  .card-meta{font-size:5.5px;line-height:8px;color:var(--muted);margin-top:2px}
  .card-actions{display:flex;justify-content:center;gap:4px;margin-top:4px}
  .card-actions span{font-size:5.5px;padding:3px 6px}
  .add{background:#e4e4e4;color:#444;border:1px solid #ccc}
  .buy{background:var(--pink);color:var(--white)}

  /* footer */
  .footer{left:0;top:980px;width:719px;height:220px;background:var(--footer)}
  .f-col{position:absolute;top:18px;font-size:6px;line-height:10px;color:#666}
  .f-col h4{font-size:7.5px;font-weight:700;color:#444;margin-bottom:4px;letter-spacing:.3px}
  .f-col h4.sp{margin-top:8px}
  .socials{display:flex;gap:4px;margin:2px 0 6px}
  .socials span{width:13px;height:13px;border-radius:50%;background:#555}
  .f-input{width:118px;height:15px;background:var(--white);border:1px solid #ccc;font-size:6px;color:#aaa;padding:3px 5px;display:inline-block;vertical-align:middle}
  .f-btn{font-size:6px;padding:4px 8px;vertical-align:middle}
  .cards{display:flex;gap:4px;margin-top:10px}
  .cards span{width:26px;height:16px;border-radius:2px}
  .copyright{position:absolute;left:0;right:0;bottom:8px;text-align:center;font-size:6px;color:#888}
</style>
</head>
<body>
<div class="page">

  <header>
    <div class="abs brand"><span class="brand-dot"></span><span class="brand-name">762petals.com</span></div>
    <div class="abs util-links"><span>Sign In</span><span>|</span><span>Cart</span><span>|</span><span>Help</span></div>
    <nav class="abs main-nav">
      <a class="active" href="#">Home</a>
      <a href="#">Shop Flowers</a>
      <a href="#">Keep Me Near</a>
      <a href="#">Recent News</a>
    </nav>
  </header>

  <section class="abs hero" role="img" aria-label="White lilies and red roses arranged across the banner">
    <div class="hero-copy">
      <h1 class="hero-title">WE SHIP EXCLUSIVELY<br>TO THE PHILIPPINES.</h1>
      <span class="btn hero-btn">SHOP NOW</span>
    </div>
  </section>

  <section class="abs info" style="left:28px">
    <h3>Recent News</h3>
    <div class="news-item"><div class="news-date">MAY<b>31</b></div><div class="news-thumb" role="img" aria-label="Customer photo"></div><div class="news-text"><strong>Lorem ipsum dolor sit amet</strong>Nulla facilisi morbi tempus etiam.</div></div>
    <div class="news-item"><div class="news-date">MAY<b>26</b></div><div class="news-thumb" role="img" aria-label="Customer photo"></div><div class="news-text"><strong>Lorem ipsum dolor sit amet</strong>Nulla facilisi morbi tempus etiam.</div></div>
    <div class="news-item"><div class="news-date">MAY<b>18</b></div><div class="news-thumb" role="img" aria-label="Customer photo"></div><div class="news-text"><strong>Lorem ipsum dolor sit amet</strong>Nulla facilisi morbi tempus etiam.</div></div>
  </section>

  <section class="abs info" style="left:252px">
    <h3>Happy Customer</h3>
    <p class="quote">Lorem ipsum dolor sit amet, consectetur adipiscing elit, sed diam nonummy nibh euismod tincidunt ut laoreet dolore magna aliquam erat volutpat. Ut wisi enim ad minim veniam, quis nostrud exerci tation ullamcorper suscipit lobortis nisl ut aliquip.</p>
    <div class="quote-foot"><span class="avatar" role="img" aria-label="Customer portrait"></span><span class="arrows"><span></span><span></span></span></div>
  </section>

  <section class="abs info" style="left:476px">
    <h3>Stay Update</h3>
    <p class="quote">Lorem ipsum dolor sit amet, consectetur adipiscing elit, sed diam nonummy nibh euismod tincidunt.</p>
    <div class="email-input">Enter Your Email</div>
    <span class="btn subscribe">Subscribe</span>
  </section>

  <aside class="abs sidebar">
    <div class="side-head">Search Flowers</div>
    <ul class="side-list">
      <li><i></i>All Flowers</li>
      <li><i></i>Hot Category</li>
    </ul>
    <div class="side-head">Narrow Your Search</div>
    <div class="side-sub">By Category</div>
    <ul class="side-list">
      <li><i></i>Birthday</li>
      <li><i></i>Anniversary</li>
      <li><i></i>Congratulations</li>
      <li><i></i>Graduation</li>
      <li><i></i>Baby Shower</li>
      <li><i></i>Get Well Soon</li>
      <li><i></i>Thank You</li>
      <li><i></i>Thinking of You</li>
      <li><i></i>Love &amp; Romance</li>
    </ul>
    <div class="side-head">Color</div>
    <div class="swatches">
      <span style="background:#d32027"></span><span style="background:#f07aa0"></span><span style="background:#9a5bc4"></span><span style="background:#f39a2b"></span><span style="background:#f5d22f"></span><span style="background:#4f9d4a"></span><span style="background:#3b74c4"></span><span style="background:#eeeeee"></span>
    </div>
    <div class="side-head">Price</div>
    <div class="price-row">$19.99 – $99.99<div class="bar"></div></div>
    <div class="offer">
      <div class="offer-title">BIRTHDAY SPECIALS<br>OFFERS!</div>
      <div class="offer-img" role="img" aria-label="Basket of mixed birthday flowers"></div>
    </div>
  </aside>

  <main class="abs products">
    <div class="products-bar">FEATURED PRODUCTS</div>
    <div class="grid">
      <div class="card"><div class="card-img sun" role="img" aria-label="Sunflower bouquet"></div><div class="card-title">LOREM IPSUM DOLOR SIT AMET</div><div class="card-meta">Price: $799.00<br>In Stock<br>Quantity in basket: none</div><div class="card-actions"><span class="add">Add to Cart</span><span class="buy">Buy Now</span></div></div>
      <div class="card"><div class="card-img roses" role="img" aria-label="Red rose bouquet"></div><div class="card-title">LOREM IPSUM DOLOR SIT AMET</div><div class="card-meta">Price: $799.00<br>In Stock<br>Quantity in basket: none</div><div class="card-actions"><span class="add">Add to Cart</span><span class="buy">Buy Now</span></div></div>
      <div class="card"><div class="card-img sun" role="img" aria-label="Sunflower bouquet"></div><div class="card-title">LOREM IPSUM DOLOR SIT AMET</div><div class="card-meta">Price: $799.00<br>In Stock<br>Quantity in basket: none</div><div class="card-actions"><span class="add">Add to Cart</span><span class="buy">Buy Now</span></div></div>
      <div class="card"><div class="card-img sun" role="img" aria-label="Sunflower bouquet"></div><div class="card-title">LOREM IPSUM DOLOR SIT AMET</div><div class="card-meta">Price: $799.00<br>In Stock<br>Quantity in basket: none</div><div class="card-actions"><span class="add">Add to Cart</span><span class="buy">Buy Now</span></div></div>
      <div class="card"><div class="card-img roses" role="img" aria-label="Red rose bouquet"></div><div class="card-title">LOREM IPSUM DOLOR SIT AMET</div><div class="card-meta">Price: $799.00<br>In Stock<br>Quantity in basket: none</div><div class="card-actions"><span class="add">Add to Cart</span><span class="buy">Buy Now</span></div></div>
      <div class="card"><div class="card-img sun" role="img" aria-label="Sunflower bouquet"></div><div class="card-title">LOREM IPSUM DOLOR SIT AMET</div><div class="card-meta">Price: $799.00<br>In Stock<br>Quantity in basket: none</div><div class="card-actions"><span class="add">Add to Cart</span><span class="buy">Buy Now</span></div></div>
    </div>
  </main>

  <footer class="abs footer">
    <div class="f-col" style="left:44px">
      <h4>ABOUT</h4>
      About 762petals<br>About the Team<br>Blog<br>Press<br>Privacy Policy<br>Site Map
      <h4 class="sp">ORDER</h4>
      Place an Order<br>Bulk Orders/Events<br>For Businesses
    </div>
    <div class="f-col" style="left:186px">
      <h4>CUSTOMER CARE</h4>
      Testimonials<br>FAQ<br>Customer Service<br>Replacement &amp; Refund Policy<br>Flower Care
      <h4 class="sp">WORKING WITH US</h4>
      Affiliates<br>For Florists<br>Contact Us
    </div>
    <div class="f-col" style="left:336px">
      <h4>FOLLOW US</h4>
      <div class="socials"><span></span><span></span><span></span><span></span><span></span></div>
      <h4 class="sp">OCCASIONS / EVENTS</h4>
      Birthday<br>Anniversary<br>Weddings<br>Holidays<br>Sympathy
    </div>
    <div class="f-col" style="left:486px">
      <h4>KEEP IN TOUCH</h4>
      <span class="f-input">Enter Your Email</span> <span class="btn f-btn">Subscribe</span>
      <div class="cards"><span style="background:#e8a23a"></span><span style="background:#2a5aa8"></span><span style="background:#5c8fd6"></span><span style="background:#4a4a4a"></span></div>
    </div>
    <div class="copyright">Copyright © 762petals.com.ph All rights reserved</div>
  </footer>

</div>
</body>
</html>
```